R & T Summit Construction Business Card ideas

We want a business card to represents our company in a way that looks professional but is also a business card that is unique!

Industry/Entity Type

Construction Company

Contact Information for Business Card

open to all design ideas, just want to be able to see different options to choose from in either color or grayscale.

Requirements
Must have
• Our names and phone numbers
• Nolan Pritchett 512-804-2271
• Curtis Hale 512-693-1804
• Business logo

```html
<!DOCTYPE html>
<html lang="en">
<head>
<meta charset="utf-8">
<title>R &amp; T Summit Construction — Business Card</title>
<link href="https://fonts.googleapis.com/css2?family=Roboto:wght@400;700&display=swap" rel="stylesheet">
<style>
  :root {
    --canvas: #e4e2de;
    --card: #ffffff;
    --card-shade: #f1f1f1;
    --ink: #111111;
    --muted: #555555;
    --rule: #1a1a1a;
    --band: #0c0c0c;
  }
  * { box-sizing: border-box; margin: 0; padding: 0; }
  html, body {
    width: 1200px; height: 1026px; overflow: hidden;
    background: var(--canvas);
    font-family: "Roboto", Arial, sans-serif;
    color: var(--ink);
  }
  .canvas {
    position: relative; width: 1200px; height: 1026px;
    display: flex; flex-direction: column; align-items: center; justify-content: center; gap: 70px;
  }
  .card {
    position: relative; width: 700px; height: 400px;
    background: linear-gradient(135deg, var(--card) 0%, var(--card-shade) 100%);
    box-shadow: 0 6px 18px rgba(0,0,0,.18);
    overflow: hidden;
  }
  .brand-name {
    font-family: "Roboto", Arial, sans-serif;
    font-weight: 700; color: var(--ink);
    text-transform: uppercase; letter-spacing: .04em; line-height: 1.15;
    display: flex; align-items: center; gap: 12px;
  }
  .brand-mark { width: 14px; height: 14px; background: var(--ink); flex: none; }

  /* front */
  .card-front .brand-name { position: absolute; left: 48px; top: 56px; font-size: 22px; width: 280px; }
  .person { position: absolute; right: 56px; top: 70px; text-align: right; }
  .person-name { font-size: 28px; font-weight: 700; }
  .person-title { font-size: 18px; color: var(--muted); margin-top: 4px; }
  .divider { position: absolute; left: 300px; right: 56px; top: 150px; height: 2px; background: var(--rule); }
  .divider-down { position: absolute; left: 300px; top: 150px; width: 2px; height: 150px; background: var(--rule); transform-origin: top; }
  .address { position: absolute; right: 56px; top: 172px; text-align: right; font-size: 15px; color: var(--muted); line-height: 1.4; }
  .contacts { position: absolute; left: 48px; bottom: 70px; list-style: none; font-size: 16px; color: var(--muted); }
  .contacts li { display: flex; align-items: center; gap: 10px; margin-top: 6px; }
  .contacts svg { width: 18px; height: 18px; flex: none; }
  .base-band { position: absolute; left: 0; right: 0; bottom: 0; height: 36px; background: var(--band); }

  /* back */
  .card-back { display: flex; align-items: center; justify-content: center; }
  .card-back .brand-name { font-size: 30px; }
  .card-back .brand-mark { width: 18px; height: 18px; }
</style>
</head>
<body>
<main class="canvas">
  <section class="card card-front" aria-label="Business card front">
    <div class="brand-name"><span class="brand-mark"></span><span>R &amp; T Summit Construction</span></div>
    <div class="person">
      <p class="person-name">Nolan Pritchett</p>
      <p class="person-title">Managing Director</p>
    </div>
    <div class="divider"></div>
    <div class="divider-down"></div>
    <p class="address">Here your company or<br>home address</p>
    <ul class="contacts">
      <li>
        <svg viewBox="0 0 20 20"><circle cx="10" cy="10" r="10" fill="#111"/><path d="M7 5.5l2 2-1 1.3c.6 1.3 1.5 2.2 2.8 2.8l1.2-1 2 2-1.2 1.4c-3.6-.4-6.7-3.5-7.1-7.1z" fill="#fff"/></svg>
        <span>512-804-2271</span>
      </li>
      <li>
        <svg viewBox="0 0 20 20"><circle cx="10" cy="10" r="10" fill="#111"/><rect x="5" y="6.5" width="10" height="7" fill="none" stroke="#fff" stroke-width="1.2"/><path d="M5 6.5l5 4 5-4" fill="none" stroke="#fff" stroke-width="1.2"/></svg>
        <span>info@rtsummit.com</span>
      </li>
      <li>
        <svg viewBox="0 0 20 20"><circle cx="10" cy="10" r="10" fill="#111"/><circle cx="10" cy="10" r="5" fill="none" stroke="#fff" stroke-width="1.2"/><path d="M5 10h10M10 5c-2.5 3-2.5 7 0 10M10 5c2.5 3 2.5 7 0 10" fill="none" stroke="#fff" stroke-width="1"/></svg>
        <span>www.rtsummitbuild.com</span>
      </li>
    </ul>
    <div class="base-band"></div>
  </section>

  <section class="card card-back" aria-label="Business card back">
    <div class="brand-name"><span class="brand-mark"></span><span>R &amp; T Summit Construction</span></div>
  </section>
</main>
</body>
</html>
```